Classy business card for accounting firm

We're looking for a new business card for our accounting firm. Our logo was designed by Brandolith, so all of the design info we would like to use has been provided. The specific font provided isn't required to be used.

We want the card to look classy and elegent. Probably more minimalistic, but still with some pops of color.

The options we would like to include on the card are as follows:
1. Main office phone line
2. Direct phone line
3. Email address
4. Website URL
5. Name
6. Title (CEO, President, etc.)
7. Firm Address

The design and card should be double sided!!! The drop down box in the project brief for some reason is defaulting to single sided. Not sure why this is happening.

Thanks!

Contact Information for Business Card

The options we would like to include on the card are as follows: 1. Main office phone line 2. Direct phone line 3. Email address 4. Website URL 5. Name 6. Title (CEO, President, etc.) 7. Firm Address

Requirements
Must have
• Card must be double sided.

```html
<!DOCTYPE html>
<html lang="en">
<head>
<meta charset="utf-8">
<title>Ledgerwell Partners – Business Card</title>
<link href="https://fonts.googleapis.com/css2?family=Poppins:wght@400;500;600&display=swap" rel="stylesheet">
<style>
  :root {
    --stage: #2b2b2b;
    --card-white: #ffffff;
    --card-dark: #3c3c3c;
    --card-dark-edge: #2a2a2a;
    --card-silver: #9a9a9a;
    --card-mid: #5a5a5a;
    --orange: #ff7a00;
    --green: #a8b932;
    --ink: #3a3a3a;
    --ink-soft: #555555;
    --silver: #ededed;
    --rule: #bdbdbd;
  }
  * { box-sizing: border-box; margin: 0; padding: 0; }
  html, body { width: 1200px; height: 689px; overflow: hidden; }
  body {
    background: var(--stage);
    font-family: "Poppins", sans-serif;
    position: relative;
  }
  .card {
    position: absolute;
    top: 190px;
    width: 540px;
    height: 309px;
    border-radius: 22px;
    overflow: hidden;
  }

  /* ---------- back side ---------- */
  .card-back { left: 30px; background: var(--card-dark); }
  .back-pattern {
    position: absolute; inset: 0;
    background:
      radial-gradient(ellipse 70% 60% at 85% 0%, rgba(235,235,235,0.55), transparent 70%),
      linear-gradient(200deg, var(--card-silver) 0%, var(--card-mid) 40%, var(--card-dark) 65%, var(--card-dark-edge) 100%);
  }
  .back-brand {
    position: absolute; left: 0; right: 0; top: 118px;
    text-align: center; color: var(--silver);
  }

  /* ---------- shared brand lockup ---------- */
  .brand-name {
    display: inline-flex; align-items: center; gap: 10px;
    font-size: 24px; font-weight: 500; letter-spacing: 2px;
  }
  .brand-square { width: 14px; height: 14px; background: var(--orange); }
  .brand-tagline {
    display: flex; align-items: center; justify-content: center; gap: 10px;
    margin-top: 4px; font-size: 9.5px; letter-spacing: 2.5px; font-weight: 500;
  }
  .brand-tagline::before, .brand-tagline::after {
    content: ""; width: 46px; height: 1px; background: var(--green);
  }

  /* ---------- front side ---------- */
  .card-front { left: 630px; background: var(--card-white); }
  .front-brand {
    position: absolute; left: 8px; width: 240px; top: 122px;
    text-align: center; color: var(--ink);
  }
  .front-brand .brand-name { font-size: 15.5px; letter-spacing: 1.3px; gap: 7px; }
  .front-brand .brand-square { width: 10px; height: 10px; }
  .front-brand .brand-tagline { font-size: 7px; letter-spacing: 2px; }
  .front-brand .brand-tagline::before, .front-brand .brand-tagline::after { width: 30px; }

  .divider {
    position: absolute; left: 258px; top: 36px; width: 1px; height: 170px;
    background: linear-gradient(var(--rule), var(--rule) 80%, transparent);
  }
  .contact { position: absolute; left: 282px; top: 32px; right: 16px; color: var(--ink); }
  .person-name { color: var(--orange); font-size: 19px; font-weight: 600; letter-spacing: 0.5px; line-height: 1.1; }
  .person-title { font-size: 12px; color: var(--ink-soft); margin-bottom: 12px; }
  .contact-list { list-style: none; font-size: 11.5px; line-height: 1.6; }
  .contact-list li { display: flex; align-items: center; gap: 8px; }
  .contact-list svg { width: 12px; height: 12px; flex: none; }
  .direct { color: var(--orange); }
  .address { margin-top: 10px; padding-left: 20px; font-size: 11.5px; line-height: 1.45; }

  .footer-band {
    position: absolute; left: 0; right: 0; bottom: 0; height: 38px;
    background: var(--orange);
    border-top: 5px solid var(--card-white);
    box-shadow: 0 -3px 0 var(--green);
  }
</style>
</head>
<body>

  <section class="card card-back" aria-label="Card back">
    <div class="back-pattern" role="img" aria-label="Embossed repeating brand pattern, silver highlights fading to charcoal"></div>
    <div class="back-brand">
      <div class="brand-name"><span class="brand-square"></span>LEDGERWELL PARTNERS</div>
      <div class="brand-tagline">SOLVING TAX PROBLEMS</div>
    </div>
  </section>

  <section class="card card-front" aria-label="Card front">
    <div class="front-brand">
      <div class="brand-name"><span class="brand-square"></span>LEDGERWELL PARTNERS</div>
      <div class="brand-tagline">SOLVING TAX PROBLEMS</div>
    </div>

    <div class="divider"></div>

    <div class="contact">
      <div class="person-name">MARCUS HALE</div>
      <div class="person-title">President</div>
      <ul class="contact-list">
        <li>
          <svg viewBox="0 0 24 24"><path fill="#a8b932" d="M6.6 10.8a15 15 0 0 0 6.6 6.6l2.2-2.2a1 1 0 0 1 1-.25 11.4 11.4 0 0 0 3.6.57 1 1 0 0 1 1 1V20a1 1 0 0 1-1 1A17 17 0 0 1 3 4a1 1 0 0 1 1-1h3.5a1 1 0 0 1 1 1c0 1.25.2 2.45.57 3.57a1 1 0 0 1-.25 1z"/></svg>
          044-555 010 234
        </li>
        <li>
          <svg viewBox="0 0 24 24"><path fill="#a8b932" d="M6.6 10.8a15 15 0 0 0 6.6 6.6l2.2-2.2a1 1 0 0 1 1-.25 11.4 11.4 0 0 0 3.6.57 1 1 0 0 1 1 1V20a1 1 0 0 1-1 1A17 17 0 0 1 3 4a1 1 0 0 1 1-1h3.5a1 1 0 0 1 1 1c0 1.25.2 2.45.57 3.57a1 1 0 0 1-.25 1z"/></svg>
          044-555 010 789 <span class="direct">(Direct)</span>
        </li>
        <li>
          <svg viewBox="0 0 24 24"><rect x="2" y="5" width="20" height="14" rx="1" fill="#a8b932"/><path d="M2 6l10 7 10-7" fill="none" stroke="#fff" stroke-width="1.6"/></svg>
          info@ledgerwell.com
        </li>
        <li>
          <svg viewBox="0 0 24 24" fill="none" stroke="#a8b932" stroke-width="2"><circle cx="12" cy="12" r="9"/><path d="M3 12h18M12 3c3 3 3 15 0 18M12 3c-3 3-3 15 0 18"/></svg>
          www.ledgerwell.com
        </li>
      </ul>
      <p class="address">18, Harbour Row, Suite 4<br>60817, Northland</p>
    </div>

    <div class="footer-band"></div>
  </section>

</body>
</html>
```